Healthcare Technology Company Business Card Design

Hi,

We require a new business card design thats catchy and professional.
Our target audience is healthcare professionals. See supplied artwork for our logo.

If you think its achievable please try add the tag line, not necessary however.
"Building smarter tools that support clinical teams and simplify daily practice"

We'll require the following information on the card. No need to have the subject titles but i've referenced them for your convenience.

Personal Details
Mark Towler
Position: Director
Phone Number - 03 9471 5382
Mobile Number - 0427 836 259
Email: firstname.lastname@velkarin.com.au

Company Details
Suite 38, 216 Wendrell Street
Kelmont Bay, Eastland
Fax: 03 8214 3975
velkarin.com.au

Prefer a thinner design than the normal stock standard business card dimensions.
Please ensure there is adequate bleed.

Target Market(s)

Healthcare Professionals

Industry/Entity Type

Healthcare

Font styles to use
Sans Serif

Requirements
Must have
• Clean, Sharp Looks
Should not have
• Any healthcare symbols

```html
<!DOCTYPE html>
<html lang="en">
<head>
<meta charset="utf-8">
<title>Velkarin Business Card</title>
<link rel="stylesheet" href="https://fonts.googleapis.com/css2?family=Open+Sans:wght@400;600;700&display=swap">
<style>
  :root {
    --navy: #1b3566;
    --navy-line: #3a5488;
    --orange: #ee7d1e;
    --card-white: #ffffff;
    --backdrop: #e9eaec;
    --text-light: #ffffff;
    --text-soft: #c9d3e6;
  }
  * { box-sizing: border-box; margin: 0; padding: 0; }
  html, body { width: 1200px; height: 900px; overflow: hidden; }
  body {
    background: var(--backdrop);
    font-family: "Open Sans", Arial, sans-serif;
    position: relative;
  }
  .card {
    position: absolute;
    left: 310px;
    width: 580px;
    height: 310px;
    box-shadow: 0 10px 30px rgba(0,0,0,0.12);
    overflow: hidden;
  }
  .card--front { top: 100px; background: var(--card-white); }
  .card--back  { top: 490px; background: var(--navy); }

  .brand {
    position: absolute;
    top: 52px;
    left: 0; right: 0;
    display: flex;
    justify-content: center;
    align-items: center;
    gap: 14px;
  }
  .brand__dot {
    width: 30px; height: 30px;
    border-radius: 50%;
    background: var(--orange);
  }
  .brand__name {
    font-size: 46px;
    font-weight: 700;
    color: var(--navy);
    letter-spacing: -1px;
    line-height: 1;
  }

  .details {
    position: absolute;
    left: 0; right: 0;
    top: 146px;
    height: 134px;
    background: var(--navy);
    display: flex;
    color: var(--text-light);
  }
  .details__col {
    flex: 1;
    padding: 20px 0 0 30px;
  }
  .details__col--company {
    border-left: 1px solid var(--navy-line);
    margin: 12px 0;
    padding-top: 8px;
  }
  .person__name {
    font-size: 15px;
    font-weight: 600;
    letter-spacing: 0.5px;
    text-transform: uppercase;
  }
  .person__role {
    font-size: 12px;
    color: var(--orange);
    margin-bottom: 8px;
  }
  .address {
    font-size: 11.5px;
    line-height: 1.45;
    margin-bottom: 12px;
    color: var(--text-soft);
  }
  .contact-list { list-style: none; }
  .contact-list li {
    display: flex;
    align-items: center;
    gap: 8px;
    font-size: 11.5px;
    line-height: 1.6;
    color: var(--text-soft);
  }
  .contact-list svg { width: 10px; height: 10px; flex: none; }

  .tagline {
    position: absolute;
    left: 0; right: 0;
    top: 200px;
    text-align: center;
    font-size: 12px;
    color: var(--text-light);
    letter-spacing: 0.2px;
  }
</style>
</head>
<body>

<section class="card card--front" aria-label="Business card front">
  <div class="brand">
    <span class="brand__dot"></span>
    <span class="brand__name">Velkarin</span>
  </div>

  <div class="details">
    <div class="details__col details__col--person">
      <p class="person__name">Mark Towler</p>
      <p class="person__role">Director</p>
      <ul class="contact-list">
        <li>
          <svg viewBox="0 0 10 10" aria-hidden="true"><path fill="#ee7d1e" d="M2 0h2l1 2.5-1.3 1a6 6 0 0 0 2.8 2.8l1-1.3L10 6v2a2 2 0 0 1-2 2A8 8 0 0 1 0 2a2 2 0 0 1 2-2z"/></svg>
          03 9471 5382
        </li>
        <li>
          <svg viewBox="0 0 10 10" aria-hidden="true"><rect x="2.5" y="0" width="5" height="10" rx="1" fill="#ee7d1e"/><rect x="3.5" y="1.2" width="3" height="6" fill="#1b3566"/></svg>
          0427 836 259
        </li>
        <li>
          <svg viewBox="0 0 10 10" aria-hidden="true"><rect x="0" y="1.5" width="10" height="7" rx="1" fill="#ee7d1e"/><path d="M0.5 2l4.5 3.5L9.5 2" fill="none" stroke="#1b3566" stroke-width="1"/></svg>
          m.towler@velkarin.com.au
        </li>
      </ul>
    </div>

    <div class="details__col details__col--company">
      <p class="address">Suite 38, 216 Wendrell Street<br>Kelmont Bay, Eastland</p>
      <ul class="contact-list">
        <li>
          <svg viewBox="0 0 10 10" aria-hidden="true"><rect x="2" y="0" width="6" height="4" fill="#ee7d1e"/><rect x="0" y="3.5" width="10" height="5" rx="1" fill="#ee7d1e"/><rect x="2" y="6.5" width="6" height="3.5" fill="#ee7d1e" stroke="#1b3566" stroke-width="0.8"/></svg>
          03 8214 3975
        </li>
        <li>
          <svg viewBox="0 0 10 10" aria-hidden="true"><circle cx="5" cy="5" r="4.5" fill="#ee7d1e"/><path d="M0.5 5h9M5 0.5v9M5 0.5c-2.4 2.5-2.4 6.5 0 9M5 0.5c2.4 2.5 2.4 6.5 0 9" fill="none" stroke="#1b3566" stroke-width="0.7"/></svg>
          velkarin.com.au
        </li>
      </ul>
    </div>
  </div>
</section>

<section class="card card--back" aria-label="Business card back">
  <p class="tagline">“Building smarter tools that support clinical teams and simplify daily practice”</p>
</section>

</body>
</html>
```